Moder Business Card Design for Renewables Business

Need a business card design for my business. We collect & repurpose spent coffee ground from cafes. The cards will be made from recycled paper. Needs to fit our corporate colour scheme of white, green & brown (see logo for colour codes). Eco friendly, modern, intresting & eye catching.
This card needs to convey the message of the business and fit into its mantra of eco-friendly, sustainable etc.

Target Market(s)

Cafe Owners, Coffee Drinkers, Recycling Companies, Farmers

Industry/Entity Type

Recycling

Contact Information for Business Card

Name; Peter Halloran
Phone; 0412 386 527
e-mail; info@lumatrove.com.au
website; www.lumatrove.com.au

Font styles to use
Sans Serif
Script

Colors

Designer to choose colors to be used in the design.

Requirements
Must have
• FRONT;
• Logo, Name (Peter Halloran), phone number, e-mail address, website
• BACK;
• On the back in cursive text; 'SUSTAINABILITY IN THE DAILY GRIND'
• Small facebook & Instagram logos with text 'Lumatrove'
Should not have
• messy design

```html
<!DOCTYPE html>
<html lang="en">
<head>
<meta charset="utf-8">
<title>Lumatrove Business Card</title>
<link href="https://fonts.googleapis.com/css2?family=Oswald:wght@600&family=Montserrat:wght@500;700&family=Allura&display=swap" rel="stylesheet">
<style>
  :root {
    --backdrop: #cfd5d5;
    --paper: #f1f1ef;
    --brown: #6b2f12;
    --green: #6cb33f;
    --edge: #a87f4a;
  }
  * { box-sizing: border-box; margin: 0; padding: 0; }
  html, body { width: 1200px; height: 1050px; overflow: hidden; }
  body {
    background: var(--backdrop);
    font-family: "Montserrat", Arial, sans-serif;
    color: var(--brown);
    position: relative;
  }
  .card {
    position: absolute;
    left: 210px;
    width: 780px;
    height: 440px;
    background: var(--paper);
    border-bottom: 3px solid var(--edge);
    box-shadow: 0 10px 24px rgba(60, 70, 70, 0.18);
  }
  .card--front { top: 55px; }
  .card--back { top: 555px; }

  .brand-mark {
    position: absolute;
    display: flex;
    flex-direction: column;
    align-items: center;
  }
  .brand-mark__circle {
    width: 150px;
    height: 150px;
    border-radius: 50%;
    border: 8px solid var(--brown);
  }
  .brand-mark__name {
    margin-top: 12px;
    font-family: "Montserrat", Arial, sans-serif;
    font-weight: 700;
    font-size: 34px;
    letter-spacing: 1px;
    color: var(--green);
    text-transform: uppercase;
  }
  .card--front .brand-mark { left: 70px; top: 50px; }
  .card--back .brand-mark { left: 50%; top: 70px; transform: translateX(-50%); }

  .person {
    position: absolute;
    left: 400px;
    top: 150px;
  }
  .person__name {
    font-family: "Oswald", "Arial Narrow", sans-serif;
    font-weight: 600;
    font-size: 40px;
    text-transform: uppercase;
    letter-spacing: 0.5px;
    margin-bottom: 18px;
  }
  .contact-list { list-style: none; }
  .contact-list li {
    display: flex;
    align-items: center;
    gap: 12px;
    font-size: 21px;
    font-weight: 500;
    line-height: 32px;
  }
  .contact-list svg { width: 18px; height: 18px; flex: none; }

  .tagline {
    position: absolute;
    left: 70px;
    bottom: 45px;
    font-family: "Allura", cursive;
    font-size: 46px;
  }

  .social {
    position: absolute;
    left: 50%;
    top: 320px;
    transform: translateX(-50%);
    display: flex;
    align-items: center;
    gap: 14px;
  }
  .social__dot {
    width: 30px;
    height: 30px;
    border-radius: 50%;
    border: 2px solid var(--brown);
  }
  .social__handle {
    font-weight: 700;
    font-size: 24px;
  }
</style>
</head>
<body>
  <section class="card card--front" aria-label="Card front">
    <div class="brand-mark">
      <div class="brand-mark__circle"></div>
      <div class="brand-mark__name">Lumatrove</div>
    </div>

    <div class="person">
      <h1 class="person__name">Peter Halloran</h1>
      <ul class="contact-list">
        <li>
          <svg viewBox="0 0 24 24" aria-hidden="true"><path fill="var(--brown)" d="M6.6 10.8a15.1 15.1 0 0 0 6.6 6.6l2.2-2.2a1 1 0 0 1 1-.25 11.4 11.4 0 0 0 3.6.57 1 1 0 0 1 1 1V20a1 1 0 0 1-1 1A17 17 0 0 1 3 4a1 1 0 0 1 1-1h3.5a1 1 0 0 1 1 1c0 1.25.2 2.45.57 3.6a1 1 0 0 1-.25 1z"/></svg>
          0412 386 527
        </li>
        <li>
          <svg viewBox="0 0 24 24" aria-hidden="true"><rect x="2.5" y="5" width="19" height="14" fill="none" stroke="var(--brown)" stroke-width="2"/><path d="M3 6l9 7 9-7" fill="none" stroke="var(--brown)" stroke-width="2"/></svg>
          info@lumatrove.com.au
        </li>
        <li>
          <svg viewBox="0 0 24 24" aria-hidden="true"><g fill="none" stroke="var(--brown)" stroke-width="2"><circle cx="12" cy="12" r="9.5"/><ellipse cx="12" cy="12" rx="4.5" ry="9.5"/><path d="M2.5 12h19"/></g></svg>
          www.lumatrove.com.au
        </li>
      </ul>
    </div>

    <p class="tagline">Sustainability In The Daily Grind</p>
  </section>

  <section class="card card--back" aria-label="Card back">
    <div class="brand-mark">
      <div class="brand-mark__circle"></div>
      <div class="brand-mark__name">Lumatrove</div>
    </div>
    <div class="social">
      <span class="social__dot"></span>
      <span class="social__handle">Lumatrove</span>
    </div>
  </section>
</body>
</html>
```